RWM Electrical Business Card Design

Have a logo to use, just looking for design around this, would like green theme, would like symbols in place of phone, fax, email etc.

Business

RWM Electrical, Marcus Thorley, marcus@rwmelectrical.example.au, www.rwmelectrical.example.au, mobile 0491 568 342, phone (07) 3915 4280, fax (07) 3915 4280, facebook and linkedin
addresses

```html
<!DOCTYPE html>
<html lang="en">
<head>
<meta charset="utf-8">
<title>RWM Electrical Business Card</title>
<link rel="stylesheet" href="https://fonts.googleapis.com/css2?family=Questrial&family=Source+Sans+3:wght@400;600&display=swap">
<style>
  :root {
    --page-bg: #e9e9ea;
    --card-light: #ffffff;
    --card-mid: #dcdcdd;
    --card-edge: #b9b9bb;
    --brand-green: #3dbb3a;
    --ink: #1e1e1e;
    --ink-soft: #2b2b2b;
    --tone-dark: #a7a7a9;
    --white: #ffffff;
  }
  * { box-sizing: border-box; margin: 0; padding: 0; }
  html, body {
    width: 1200px; height: 900px; overflow: hidden;
    background: var(--page-bg);
  }
  .canvas { position: relative; width: 1200px; height: 900px; }
  .card {
    position: absolute; left: 250px; width: 700px; height: 400px;
    overflow: hidden;
    background: radial-gradient(ellipse at 45% 55%, var(--card-light) 0%, var(--card-mid) 70%, var(--card-edge) 100%);
    box-shadow: 0 6px 18px rgba(0,0,0,0.18);
  }
  .card--front { top: 40px; }
  .card--back { top: 460px; }

  /* front */
  .front-band { position: absolute; inset: 0; width: 700px; height: 400px; }
  .front-brand {
    position: absolute; left: 80px; top: 148px;
    font-family: "Questrial", sans-serif; font-weight: 400; font-size: 44px; color: var(--ink);
    line-height: 1; letter-spacing: 0.5px;
  }
  .front-url {
    position: absolute; left: 128px; top: 222px;
    font-family: "Source Sans 3", sans-serif; font-weight: 600;
    font-size: 18px; line-height: 1; color: var(--brand-green);
  }

  /* back */
  .back-backdrop {
    position: absolute; inset: 0;
    background: radial-gradient(ellipse at 50% 55%, var(--card-light) 0%, var(--card-mid) 60%, var(--tone-dark) 100%);
  }
  .back-brand {
    position: absolute; left: 44px; top: 38px;
    display: flex; align-items: center; gap: 8px;
    font-family: "Questrial", sans-serif; font-size: 21px; line-height: 1; color: var(--ink);
  }
  .back-brand__dot {
    width: 20px; height: 20px; border-radius: 50%; background: var(--ink-soft);
  }
  .name-band {
    position: absolute; left: 46px; top: 76px; width: 620px; height: 46px;
    background: var(--brand-green);
    display: flex; align-items: center; justify-content: flex-end; padding-right: 16px;
  }
  .name-band__name {
    font-family: "Questrial", sans-serif; font-weight: 400; font-size: 32px; line-height: 1; color: var(--white);
  }
  .contact-list {
    position: absolute; left: 370px; top: 180px; list-style: none;
    font-family: "Source Sans 3", sans-serif; font-size: 13px; color: var(--ink-soft);
  }
  .contact-list__item { display: flex; align-items: center; gap: 12px; height: 23px; }
  .contact-list__item--gap { margin-top: 14px; }
  .contact-list__icon { width: 18px; height: 18px; flex: none; }
  .contact-list__square {
    width: 16px; height: 16px; margin: 0 1px; flex: none; background: var(--ink-soft); border-radius: 2px;
  }
</style>
</head>
<body>
<main class="canvas">

  <section class="card card--front" aria-label="Card front">
    <svg class="front-band" viewBox="0 0 700 400" aria-hidden="true">
      <polygon points="520,0 690,0 400,400 300,400" fill="var(--brand-green)"/>
    </svg>
    <h1 class="front-brand">RWM Electrical</h1>
    <p class="front-url">www.rwmelectrical.example.au</p>
  </section>

  <section class="card card--back" aria-label="Card back">
    <div class="back-backdrop" role="img" aria-label="Soft grey decorative background"></div>

    <div class="back-brand">
      <span class="back-brand__dot"></span>
      <span>RWM Electrical</span>
    </div>

    <div class="name-band">
      <h2 class="name-band__name">Marcus Thorley</h2>
    </div>

    <ul class="contact-list">
      <li class="contact-list__item">
        <svg class="contact-list__icon" viewBox="0 0 18 18" aria-label="Phone"><path d="M2 6 Q9 1 16 6 L14 8 L12 6 L6 6 L4 8 Z" fill="var(--ink)"/><rect x="4" y="9" width="10" height="7" rx="1" fill="var(--ink)"/></svg>
        <span>(07) 3915 4280</span>
      </li>
      <li class="contact-list__item">
        <svg class="contact-list__icon" viewBox="0 0 18 18" aria-label="Mobile"><rect x="5" y="1" width="8" height="16" rx="1.5" fill="var(--ink)"/><rect x="6.3" y="3" width="5.4" height="10" fill="var(--white)"/></svg>
        <span>0491 568 342</span>
      </li>
      <li class="contact-list__item">
        <svg class="contact-list__icon" viewBox="0 0 18 18" aria-label="Fax"><rect x="5" y="1" width="8" height="6" fill="none" stroke="var(--ink)" stroke-width="1.4"/><rect x="2" y="7" width="14" height="9" rx="1" fill="var(--ink)"/><rect x="5" y="10" width="8" height="1.4" fill="var(--white)"/></svg>
        <span>(07) 3915 4280</span>
      </li>
      <li class="contact-list__item">
        <svg class="contact-list__icon" viewBox="0 0 18 18" aria-label="Email"><circle cx="9" cy="9" r="8" fill="none" stroke="var(--ink)" stroke-width="1.4"/><rect x="4.5" y="6" width="9" height="6.5" fill="none" stroke="var(--ink)" stroke-width="1.2"/><path d="M4.5 6 L9 10 L13.5 6" fill="none" stroke="var(--ink)" stroke-width="1.2"/></svg>
        <span>marcus@rwmelectrical.example.au</span>
      </li>
      <li class="contact-list__item contact-list__item--gap">
        <span class="contact-list__square" aria-hidden="true"></span>
        <span>rwmelectrical</span>
      </li>
      <li class="contact-list__item">
        <span class="contact-list__square" aria-hidden="true"></span>
        <span>marcusthorley</span>
      </li>
    </ul>
  </section>

</main>
</body>
</html>
```